Start-up Cleaning Business Needs Professional Business Cards

Marta's Butler Cleaning, LLC, is a start-up business based in the Northern Virginia suburbs of Washington, DC. MBC provides cleaning and housekeeping services for homes and offices. We have three core values:

1. We are personal. We value knowing and being known by our customers and each other. If you want nameless, faceless service, you should choose another provider. We put "personal" at the front of the list, because it is most important to us; the design we choose will convey this value.

2. Like a hotel concierge, we are professional in attitude, posture, communication and processes.

3. Like a hotel concierge, we solve problems with a can-do attitude and never make excuses.

Our uniforms are khaki pants with pink polo shirts.

Our logo is attached. There are other symbols, not represented in our logo, that may convey our values well, such as a top hat and bow tie, magnifying glass, desk bell, etc.

Please include fields for an individual's name and title, office phone number, mobile phone number, email address and website address (www.martasbutlercleaning.example).

Standard U.S. size: 2" x 3.5"
Updates

I should have mentioned that the purpose of all our advertising - business cards included - is to motivate potential customers to call or email to arrange a free in-home estimate.

```html
<!DOCTYPE html>
<html lang="en">
<head>
<meta charset="utf-8">
<title>Marta's Butler Cleaning – Business Cards</title>
<link rel="stylesheet" href="https://fonts.googleapis.com/css2?family=Lato:wght@400;700&display=swap">
<style>
  :root {
    --canvas: #e6e6e8;
    --card-white: #ffffff;
    --card-pink: #f8e3ec;
    --magenta: #e8388e;
    --magenta-soft: #f6c9dc;
    --ink: #222222;
    --logo-ink: #4a4a4a;
    --muted: #8a8a8a;
    --art-light: #f3d2e1;
    --art-dark: #c9a6a0;
  }
  * { box-sizing: border-box; margin: 0; padding: 0; }
  html, body {
    width: 1200px; height: 926px; overflow: hidden;
    background: var(--canvas);
    font-family: "Lato", Arial, sans-serif;
  }
  .sheet {
    width: 1200px; height: 926px;
    display: flex; flex-direction: column; align-items: center; justify-content: center;
    gap: 46px;
  }
  .card {
    position: relative;
    width: 700px; height: 400px;
    background: radial-gradient(ellipse at 40% 45%, var(--card-white) 0%, var(--card-pink) 85%);
    box-shadow: 0 6px 18px rgba(0,0,0,.18);
    overflow: hidden;
  }
  /* front */
  .card-front .art {
    position: absolute; left: 265px; top: 50px; width: 170px; height: 200px;
  }
  .card-front .brand {
    position: absolute; left: 0; right: 0; top: 262px; text-align: center; color: var(--logo-ink);
  }
  .brand-name { font-size: 40px; font-weight: 400; line-height: 1; }
  .brand-tag { font-size: 13px; font-weight: 400; letter-spacing: 3px; margin-top: 6px; }
  /* back */
  .card-back .brand { position: absolute; left: 48px; top: 40px; color: var(--logo-ink); }
  .card-back .brand-name { font-size: 36px; }
  .card-back .brand-tag { font-size: 12px; margin-top: 5px; }
  .person { position: absolute; left: 48px; top: 150px; }
  .person-name { font-size: 30px; color: var(--magenta); font-weight: 400; line-height: 1; }
  .person-name b { font-weight: 700; }
  .person-title { font-size: 15px; color: var(--ink); margin-top: 4px; }
  .contacts { position: absolute; left: 48px; top: 232px; list-style: none; font-size: 16px; color: var(--ink); line-height: 27px; }
  .contacts b { font-weight: 700; }
  .card-back .art {
    position: absolute; left: 455px; top: 95px; width: 215px; height: 260px;
  }
  .band { position: absolute; left: 0; right: 0; bottom: 18px; height: 12px; background: var(--magenta); }
  .band-under { position: absolute; left: 0; right: 0; bottom: 0; height: 18px; background: var(--magenta-soft); }
</style>
</head>
<body>
<main class="sheet">
  <section class="card card-front">
    <svg class="art" viewBox="0 0 170 200" role="img" aria-label="Sketch illustration of a housekeeper in pink uniform mopping the floor">
      <defs>
        <linearGradient id="artFront" x1="0" y1="0" x2="0" y2="1">
          <stop offset="0" stop-color="var(--art-dark)" stop-opacity=".35"/>
          <stop offset="1" stop-color="var(--art-light)" stop-opacity=".8"/>
        </linearGradient>
      </defs>
      <rect width="170" height="200" rx="10" fill="url(#artFront)"/>
    </svg>
    <div class="brand">
      <div class="brand-name">Marta's</div>
      <div class="brand-tag">Butler Cleaning</div>
    </div>
  </section>

  <section class="card card-back">
    <div class="brand">
      <div class="brand-name">Marta's</div>
      <div class="brand-tag">Butler Cleaning</div>
    </div>
    <div class="person">
      <div class="person-name">dana <b>reyes</b></div>
      <div class="person-title">product manager</div>
    </div>
    <ul class="contacts">
      <li><b>mobile</b>: 0123456789</li>
      <li><b>office</b> phone: 055-010-4482</li>
      <li><b>web</b>: www.martasbutlercleaning.example</li>
      <li><b>email</b>: dana@martasbutlercleaning.example</li>
    </ul>
    <svg class="art" viewBox="0 0 215 260" role="img" aria-label="Sketch illustration of a housekeeper in pink uniform mopping the floor">
      <defs>
        <linearGradient id="artBack" x1="0" y1="0" x2="0" y2="1">
          <stop offset="0" stop-color="var(--art-dark)" stop-opacity=".35"/>
          <stop offset="1" stop-color="var(--art-light)" stop-opacity=".8"/>
        </linearGradient>
      </defs>
      <rect width="215" height="260" rx="12" fill="url(#artBack)"/>
    </svg>
    <div class="band"></div>
    <div class="band-under"></div>
  </section>
</main>
</body>
</html>
```